Anzeigengestaltung für Brötchen- und Brotlieferant
Zielgruppe
Wir beliefern Privatkunden Freitag, Samstag und Sonntag mit Brötchen / Broten und suchen ein Design für eine Werbekampagne zur Neukundengewinnung über Facebook. Sprich ein Bild indem alles kurz und knapp für den Kunden erklärt wird und man damit Werbung schalten kann.

```html
<!DOCTYPE html>
<html lang="de">
<head>
<meta charset="utf-8">
<title>Brötchen Lieferservice – Anzeige</title>
<link href="https://fonts.googleapis.com/css2?family=Roboto+Slab:wght@300;400;700&family=Nothing+You+Could+Do&display=swap" rel="stylesheet">
<style>
  :root {
    --brown: #7a3121;
    --peach: #f5c38a;
    --cream: #fbe9d6;
    --ink: #3a2a24;
    --wood: #f4f3f1;
  }
  * { margin: 0; padding: 0; box-sizing: border-box; }
  html, body { width: 1200px; height: 1200px; overflow: hidden; }
  body { font-family: "Roboto Slab", serif; background: var(--wood); }
  .ad { position: relative; width: 1200px; height: 1200px; overflow: hidden; }

  .backdrop {
    position: absolute; inset: 0;
    background:
      radial-gradient(ellipse 330px 520px at 1090px 520px, #d99a55 0%, #e7b47a 45%, rgba(244,243,241,0) 100%),
      radial-gradient(ellipse 260px 170px at 760px 90px, #e4a963 0%, rgba(244,243,241,0) 100%),
      repeating-linear-gradient(180deg, #f7f6f4 0 58px, #ecebe8 58px 60px);
  }

  .brand {
    position: absolute; left: 63px; top: 120px; width: 200px;
    display: flex; align-items: center; gap: 10px;
    color: var(--brown); font-weight: 400; font-size: 22px; line-height: 1.1;
  }
  .brand-dot { width: 40px; height: 40px; border-radius: 50%; background: var(--peach); flex: none; }

  .headline {
    position: absolute; left: 60px; top: 262px;
    color: var(--brown); font-weight: 700; font-size: 118px; line-height: 122px;
    letter-spacing: -1px;
  }
  .intro {
    position: absolute; left: 62px; top: 520px; width: 745px;
    color: var(--ink); font-weight: 300; font-size: 36px; line-height: 52px;
    text-align: justify;
  }

  .benefits { position: absolute; left: 59px; top: 683px; list-style: none; }
  .benefit {
    width: 567px; height: 82px; margin-bottom: 21px;
    background: var(--brown); color: #fff;
    border-radius: 12px 34px 12px 12px;
    display: flex; align-items: center; padding-left: 22px; gap: 20px;
    font-weight: 700; font-size: 33px;
  }
  .benefit svg { flex: none; }

  .offer {
    position: absolute; left: 855px; top: 66px; width: 300px; height: 300px;
    border-radius: 50%; background: var(--brown);
    transform: rotate(5deg);
    display: flex; flex-direction: column; align-items: center; justify-content: center;
    color: var(--cream); text-align: center;
  }
  .offer::after {
    content: ""; position: absolute; inset: 7px; border-radius: 50%;
    border: 1.5px solid var(--cream); opacity: .8;
  }
  .offer-now { font-weight: 300; font-size: 54px; line-height: 56px; }
  .offer-free { font-weight: 700; font-size: 54px; line-height: 52px; }
  .offer-try { font-weight: 700; font-size: 37px; line-height: 42px; }
  .offer-note { font-weight: 400; font-size: 16px; margin-top: 10px; }

  .claim {
    position: absolute; left: 670px; top: 850px; width: 480px;
    font-family: "Nothing You Could Do", cursive;
    color: var(--brown); font-size: 34px; line-height: 48px; transform: rotate(2deg);
  }
  .claim-line1 { padding-left: 60px; }
  .claim-rule { display: block; height: 2px; background: var(--brown); margin-top: 6px; width: 450px; transform: rotate(2deg); }

  .footer { position: absolute; left: 0; top: 1040px; width: 1200px; height: 160px; }
  .footer svg { position: absolute; left: 0; top: 0; }
  .contact {
    position: absolute; left: 90px; top: 1087px;
    color: var(--cream); font-weight: 300; font-size: 22.5px; line-height: 30px;
  }
  .contact .hl { color: var(--peach); font-weight: 400; }
  .delivery-icon {
    position: absolute; left: 985px; top: 1092px; width: 125px; height: 82px;
    border-radius: 12px; background: rgba(251,233,214,.25);
  }
</style>
</head>
<body>
<main class="ad">
  <div class="backdrop" role="img" aria-label="Foto: frische Brötchen, Baguette und Weizenähren auf hellem Holztisch"></div>

  <div class="brand"><span class="brand-dot"></span><span>Brötchenservice<br>Lena Koppner</span></div>

  <h1 class="headline">Brötchen<br>Lieferservice</h1>
  <p class="intro">Wir versorgen Sie gerne von Freitag bis Sonntag mit frischen Brötchen.</p>

  <ul class="benefits">
    <li class="benefit"><svg width="40" height="38" viewBox="0 0 40 38"><rect x="2" y="6" width="30" height="30" rx="6" fill="none" stroke="#f5c38a" stroke-width="3.5"/><path d="M9 20 L17 28 L37 4" fill="none" stroke="#f5c38a" stroke-width="4.5" stroke-linecap="round" stroke-linejoin="round"/></svg>keine Mindestbestellmenge</li>
    <li class="benefit"><svg width="40" height="38" viewBox="0 0 40 38"><rect x="2" y="6" width="30" height="30" rx="6" fill="none" stroke="#f5c38a" stroke-width="3.5"/><path d="M9 20 L17 28 L37 4" fill="none" stroke="#f5c38a" stroke-width="4.5" stroke-linecap="round" stroke-linejoin="round"/></svg>kein verstecktes Abo</li>
    <li class="benefit"><svg width="40" height="38" viewBox="0 0 40 38"><rect x="2" y="6" width="30" height="30" rx="6" fill="none" stroke="#f5c38a" stroke-width="3.5"/><path d="M9 20 L17 28 L37 4" fill="none" stroke="#f5c38a" stroke-width="4.5" stroke-linecap="round" stroke-linejoin="round"/></svg>Bestellung jederzeit kündbar</li>
  </ul>

  <div class="offer">
    <span class="offer-now">Jetzt</span>
    <span class="offer-free">GRATIS</span>
    <span class="offer-try">PROBIEREN!</span>
    <span class="offer-note">5x Gratis Brötchen</span>
  </div>

  <p class="claim"><span class="claim-line1">Frühstücksbrötchen</span><br>immer knusprig und frisch!<span class="claim-rule"></span></p>

  <footer class="footer">
    <svg width="1200" height="160" viewBox="0 0 1200 160">
      <defs>
        <pattern id="scallop" width="40" height="20" patternUnits="userSpaceOnUse">
          <ellipse cx="20" cy="20" rx="20" ry="10" fill="#7a3121"/>
        </pattern>
      </defs>
      <rect x="0" y="2" width="1200" height="18" fill="url(#scallop)"/>
      <rect x="0" y="19" width="1200" height="141" fill="#7a3121"/>
    </svg>
  </footer>
  <p class="contact">
    Brötchenservice Lena Koppner • Lindenweg 14 • 02931 Waldenau<br>
    Schreiben Sie uns einfach eine E-Mail an <span class="hl">kontakt@broetchen-koppner.de</span><br>
    oder rufen Sie uns an unter <span class="hl">035870 / 12 34 56</span>.
  </p>
  <div class="delivery-icon" role="img" aria-label="Symbol: Lieferant auf Motorroller"></div>
</main>
</body>
</html>
```